Flyer for spiritual retreat (yoga, meditation, reiki, raw food)

I would like a flyer to promote my upcoming retreat and a matching Facebook banner.

The name of the retreat is "Wavecrest Of Calm" and the tagline is "retreat into you"

The activities in the retreat include daily meditation, ecstatic dance, spiritual development workshops on intuition, energy healing etc and a reiki session is included.

I would like a flyer designed to promote this, something that is editable as I will be running this multiple times and will need to adjust the flyer to add the dates etc each time.

edit: add that here will be fully catered raw food and juices, and that the retreat price includes all accomodation, meals and workshops.

Please contact me if you need further info. Please also visit my website www.marithovland.com and www.facebook.com/tolvanahaven to see my current events and promotions.

Thank you,

Marit

Reason: Hi all, thank you all for your submissions. Apologies as I am traveling and do not have much access to internet and will review your submissions and provide feedback as soon as possible. Kind regards, Marit.

Target Market(s)

People who like meditation, yoga, fans of rowan mabry and jasper vinek, those interested in personal and spiritual development.

Industry/Entity Type

Health And Wellness

Requirements
Must have
• Please put the included reiki session as as added bonus. Something like "BONUS 30 minute reiki healing session" in a little star/banner/something that stands out.
• Please emphasise the "light" part of Wavecrest as I am going for a play on words between in the light and enlightenment.
• Please include placeholder text for place, location, time
• Placeholder for price
• My name (see attached file - can change colour to suit) and website (www.marithovland.com)
Nice to have
• I prefer rounded designs, curves rather than block designs.
Should not have
• Tolvana Haven logo

```html
<!DOCTYPE html>
<html lang="en">
<head>
<meta charset="utf-8">
<title>Wavecrest Of Calm – Retreat Into You</title>
<link href="https://fonts.googleapis.com/css2?family=Great+Vibes&family=Crimson+Text:ital,wght@0,400;0,700;1,400;1,700&family=Montserrat:wght@300;600&display=swap" rel="stylesheet">
<style>
  :root {
    --sky-top: #7ba3d9;
    --sky-deep: #42649c;
    --sky-mid: #6f93c9;
    --sky-low: #b7cceb;
    --navy: #1f2a3d;
    --white: #ffffff;
    --rule: rgba(255,255,255,0.75);
    --statue-dark: #2b2f38;
    --lotus-light: #e6eefb;
  }
  * { margin: 0; padding: 0; box-sizing: border-box; }
  html, body { width: 849px; height: 1200px; overflow: hidden; background: var(--sky-low); }
  .flyer {
    position: relative;
    width: 849px;
    height: 1200px;
    overflow: hidden;
    color: var(--white);
    background: linear-gradient(180deg,
      var(--sky-top) 0px,
      var(--sky-top) 300px,
      var(--sky-deep) 420px,
      var(--sky-deep) 560px,
      var(--sky-mid) 820px,
      var(--sky-low) 1120px,
      var(--sky-low) 1177px,
      var(--navy) 1177px);
  }
  .title {
    position: absolute;
    left: 120px;
    top: 10px;
    font-family: "Great Vibes", cursive;
    font-weight: 400;
    line-height: 1;
  }
  .title-line { display: block; font-size: 128px; }
  .title-line--second { margin-left: 55px; margin-top: -8px; }
  .tagline {
    position: absolute;
    left: 413px;
    top: 290px;
    font-family: "Montserrat", sans-serif;
    font-weight: 300;
    font-size: 28px;
    letter-spacing: 1.5px;
  }
  .intro {
    position: absolute;
    left: 26px;
    top: 366px;
    width: 800px;
    font-family: "Crimson Text", serif;
    font-style: italic;
    font-size: 23px;
    line-height: 37px;
  }
  .intro strong { font-weight: 700; }
  .benefits {
    position: absolute;
    left: 31px;
    top: 542px;
    width: 800px;
    list-style: none;
    display: grid;
    grid-template-columns: 404px 1fr;
    row-gap: 9px;
    font-family: "Crimson Text", serif;
    font-size: 24px;
    line-height: 37px;
  }
  .benefits li::before { content: "✻"; margin-right: 8px; font-size: 20px; }
  .bonus {
    position: absolute;
    left: 164px;
    top: 697px;
    width: 513px;
    padding: 6px 0 5px;
    border-top: 1.5px solid var(--rule);
    border-bottom: 1.5px solid var(--rule);
    text-align: center;
    font-family: "Crimson Text", serif;
    font-weight: 700;
    font-size: 25px;
    line-height: 29px;
  }
  .details {
    position: absolute;
    left: 26px;
    top: 780px;
    font-family: "Montserrat", sans-serif;
    font-weight: 600;
    font-size: 16px;
    letter-spacing: 1.5px;
  }
  .details-row { display: flex; height: 46px; align-items: center; }
  .details-label { width: 77px; }
  .host {
    position: absolute;
    right: 29px;
    top: 765px;
    text-align: right;
  }
  .host-name {
    font-family: "Great Vibes", cursive;
    font-size: 64px;
    line-height: 1.2;
    color: var(--white);
    margin-right: 10px;
  }
  .host-web {
    margin-top: 10px;
    font-family: "Crimson Text", serif;
    font-size: 25px;
    line-height: 32px;
  }
  .host-social {
    display: flex;
    justify-content: flex-end;
    align-items: center;
    gap: 6px;
    font-family: "Crimson Text", serif;
    font-size: 25px;
    line-height: 32px;
  }
  .host-social-mark { width: 22px; height: 22px; background: var(--white); }
  .statue-art {
    position: absolute;
    left: 290px;
    top: 905px;
    width: 270px;
    height: 272px;
    border-radius: 135px 135px 0 0;
    background:
      radial-gradient(ellipse 60px 120px at 50% 70%, var(--statue-dark) 0%, rgba(43,47,56,0.85) 60%, rgba(43,47,56,0) 100%),
      radial-gradient(ellipse at 50% 55%, var(--lotus-light) 0%, rgba(230,238,251,0.5) 55%, rgba(230,238,251,0) 80%);
  }
</style>
</head>
<body>
  <main class="flyer">
    <h1 class="title">
      <span class="title-line">Wavecrest</span>
      <span class="title-line title-line--second">Of Calm</span>
    </h1>
    <p class="tagline">RETREAT INTO YOU</p>

    <p class="intro">Leave your stresses and worries behind. Come immerse yourself in the bliss of the Transcendental Self. Learn how to integrate this level of awareness into daily living for greater peace, success and happiness in life. In this special <strong>all inclusive</strong> retreat you will gain the benefits of:</p>

    <ul class="benefits">
      <li>Daily Meditation Practice</li>
      <li>Ecstatic Dance</li>
      <li>Spiritual Development</li>
      <li>Enhanced Intuition</li>
      <li>Energy Healing</li>
      <li>Fully Catered Raw Food &amp; Juices</li>
    </ul>

    <p class="bonus">BONUS 30 Minute Reiki Healing Session</p>

    <dl class="details">
      <div class="details-row"><dt class="details-label">DATE</dt><dd>:</dd></div>
      <div class="details-row"><dt class="details-label">PLACE</dt><dd>:</dd></div>
      <div class="details-row"><dt class="details-label">TIME</dt><dd>:</dd></div>
      <div class="details-row"><dt class="details-label">COST</dt><dd>:</dd></div>
    </dl>

    <div class="host">
      <p class="host-name">Marit Hovland</p>
      <p class="host-web">www.marithovland.com</p>
      <p class="host-social"><span class="host-social-mark"></span>tolvanahaven</p>
    </div>

    <div class="statue-art" role="img" aria-label="Dark seated meditating statue in front of a large white line-drawn lotus flower"></div>
  </main>
</body>
</html>
```